Security business needs NDA formatted.

We need our NDA formatted properly and to look modern with our logo. Anybody can paste words into a document, but we need something clean, modern, DocuSign-friendly, and stylish.

```html
<!DOCTYPE html>
<html lang="en">
<head>
<meta charset="utf-8">
<title>Terravane — Non-Disclosure Agreement</title>
<link href="https://fonts.googleapis.com/css2?family=Montserrat:wght@400;500;600;700;800&display=swap" rel="stylesheet">
<style>
  :root {
    --bg: #ededed;
    --paper: #ffffff;
    --ink: #3b3b3d;
    --ink-soft: #5a5a5d;
    --rule: #55565a;
    --accent: #e05064;
    --accent-deep: #c73a4f;
    --footer: #555558;
  }
  * { margin: 0; padding: 0; box-sizing: border-box; }
  html, body { width: 1200px; height: 800px; overflow: hidden; }
  body {
    background: var(--bg);
    font-family: "Montserrat", sans-serif;
    color: var(--ink);
    display: flex; align-items: center; justify-content: center;
  }
  .page {
    position: relative;
    width: 590px; height: 764px;
    background: var(--paper);
    box-shadow: 0 6px 24px rgba(0,0,0,0.12);
    overflow: hidden;
  }
  .brand {
    display: flex; align-items: center; justify-content: center;
    gap: 12px; margin-top: 46px;
  }
  .brand-mark {
    width: 46px; height: 46px; border-radius: 50%;
    background: #2f2f31;
  }
  .brand-divider { width: 1px; height: 50px; background: var(--ink); }
  .brand-name {
    font-weight: 700; font-size: 30px; color: #2f2f31; line-height: 1;
  }
  .brand-tagline {
    font-weight: 600; font-size: 9.5px; letter-spacing: 1.2px; color: var(--ink-soft);
    margin-top: 4px;
  }
  .header-rule {
    position: relative; margin: 20px 50px 0; height: 1px; background: var(--rule);
  }
  .header-rule::after {
    content: ""; position: absolute; left: 32%; width: 36%; top: -1px; height: 3px;
    background: var(--accent);
  }
  .doc-title {
    text-align: center; margin-top: 26px;
    font-weight: 800; font-size: 16px; letter-spacing: 3.5px;
  }
  .doc-body { padding: 0 60px; font-size: 11.5px; line-height: 1.65; color: var(--ink); }
  .preamble { margin-top: 18px; text-align: center; }
  .blank { display: inline-block; border-bottom: 1px solid var(--ink); width: 70px; height: 10px; }
  .label { margin-top: 12px; }
  .party { margin-top: 16px; padding-left: 28px; font-weight: 500; }
  .part-tag {
    text-align: right; font-weight: 500; font-size: 10.5px; margin-top: 6px;
  }
  .part-tag span { display: inline-block; border-bottom: 1.5px solid var(--accent); padding-bottom: 2px; }
  .and { text-align: center; font-weight: 600; margin-top: 12px; }
  .section-head {
    margin-top: 16px; font-weight: 700; font-size: 11.5px; letter-spacing: 0.5px;
  }
  .section-head::after {
    content: ""; display: block; width: 26px; height: 2px; background: var(--accent); margin-top: 3px;
  }
  .recital { margin-top: 8px; }
  .footer { position: absolute; left: 0; right: 0; bottom: 0; }
  .footer-band { height: 12px; background: linear-gradient(90deg, var(--accent-deep), var(--accent)); }
  .footer-bar {
    height: 40px; background: var(--footer); color: #f2f2f2;
    display: flex; align-items: center; justify-content: space-between;
    padding: 0 30px; font-size: 9.5px;
  }
</style>
</head>
<body>
  <main class="page">
    <header>
      <div class="brand">
        <div class="brand-mark"></div>
        <div class="brand-divider"></div>
        <div>
          <div class="brand-name">Terravane</div>
          <div class="brand-tagline">Geospatial Intelligence</div>
        </div>
      </div>
      <div class="header-rule"></div>
      <h1 class="doc-title">NON-DISCLOSURE AGREEMENT</h1>
    </header>

    <section class="doc-body">
      <p class="preamble">THIS NON-DISCLOSURE AGREEMENT ("the Agreement") dated<br>
        this <span class="blank"></span> day of <span class="blank"></span>, <span class="blank"></span>.</p>
      <p class="label">BETWEEN:</p>
      <p class="party">ACME of 48 Cedar Row, CA, 95012, USA (the "Company")</p>
      <p class="part-tag"><span>OF THE FIRST PART</span></p>
      <p class="and">- AND -</p>
      <p class="party">COMPANY NAME of COMPANY ADDRESS<br>(the "Evaluator")</p>
      <p class="part-tag"><span>OF THE SECOND PART</span></p>

      <h2 class="section-head">BACKGROUND:</h2>
      <p class="recital">A. ACME has proprietary information and know-how relating to certain investigation tools and tactics (the "Company").</p>
      <p class="recital">B. In connection with the Evaluator evaluating the Invention for possible patent, development, and marketing (the "Permitted Purpose"), the Evaluator has requested certain confidential information (the "Confidential Information") regarding the Company.</p>
    </section>

    <footer class="footer">
      <div class="footer-band"></div>
      <div class="footer-bar">
        <span>©2002-2022 DocForge.net®</span>
        <span>Page 1 of 9</span>
      </div>
    </footer>
  </main>
</body>
</html>
```